Membership Card for our Survival Company

We need a membership card design, front and back for our VIP Membership program. Membership card must be branded with our logo and convey the idea of survivalism.
All members will receive this physical, plastic card with embossed Full Name and unique Membership ID.
ID formatting: "VIP-XXXXXXX"
See example image here:
https://media.brightorbalo.com/7k/52e9a1c3b08d44f6a7c1d29e3b0f57/VIP-Membership-Card1-Reflect.png
Note, this is just an example. We do not require you to follow the size, format, image, etc. The only things that must be included are the:
1) Logo
2) Full Name
3) Membership ID as per the provided format
Any more questions, please let me know.
It Company
Full Name
VIP-XXXXXXX

```html
<!DOCTYPE html>
<html lang="en">
<head>
<meta charset="UTF-8">
<title>TrailKeeper VIP Membership Card</title>
<link rel="stylesheet" href="https://fonts.googleapis.com/css2?family=Lato:wght@700;900&display=swap">
<style>
  :root {
    --page-bg: #ffffff;
    --sky-top: #4a1f14;
    --sky-rust: #b5603f;
    --sky-glow: #c97552;
    --sky-haze: #8a5a55;
    --mist-dark: #3a2522;
    --ground-black: #050302;
    --brand-green: #c6e04a;
    --brand-orange: #f5a623;
    --name-white: #ffffff;
    --id-gold: #f6b51e;
  }
  html, body {
    margin: 0;
    padding: 0;
    width: 1195px;
    height: 1200px;
    overflow: hidden;
    background: var(--page-bg);
  }
  .membership-card {
    position: absolute;
    left: 143px;
    top: 109px;
    width: 929px;
    height: 552px;
    border-radius: 28px;
    overflow: hidden;
    font-family: "Lato", sans-serif;
    box-shadow: 0 6px 14px rgba(0, 0, 0, 0.35);
  }
  .card-scene {
    position: absolute;
    inset: 0;
    background:
      radial-gradient(ellipse 34% 60% at 12% 72%, rgba(5, 3, 2, 0.85) 0%, rgba(5, 3, 2, 0) 100%),
      radial-gradient(ellipse 45% 30% at 88% 8%, rgba(40, 20, 14, 0.8) 0%, rgba(40, 20, 14, 0) 100%),
      radial-gradient(ellipse 40% 35% at 25% 40%, rgba(201, 117, 82, 0.6) 0%, rgba(201, 117, 82, 0) 100%),
      linear-gradient(180deg,
        var(--sky-top) 0%,
        var(--sky-rust) 28%,
        var(--sky-haze) 55%,
        var(--mist-dark) 68%,
        var(--ground-black) 78%,
        var(--ground-black) 100%);
  }
  .brand {
    position: absolute;
    left: 335px;
    top: 56px;
    display: flex;
    align-items: center;
    gap: 10px;
  }
  .brand-dot {
    width: 68px;
    height: 68px;
    border-radius: 50%;
    background: var(--brand-orange);
  }
  .brand-name {
    font-weight: 700;
    font-size: 52px;
    color: var(--brand-green);
    letter-spacing: 0.5px;
  }
  .member-details {
    position: absolute;
    left: 420px;
    width: 484px;
    top: 259px;
    text-align center;
  }
  .member-name {
    margin: 0;
    font-weight: 900;
    font-size: 39px;
    line-height: 46px;
    letter-spacing: 15px;
    color: var(--name-white);
    white-space: nowrap;
    text-align: center;
  }
  .member-id {
    margin: 6px 0 0;
    font-weight: 900;
    font-size: 40px;
    line-height: 46px;
    color: var(--id-gold);
    text-align: center;
  }
</style>
</head>
<body>
  <div class="membership-card">
    <div class="card-scene" role="img" aria-label="Photo of a hiker with backpack and trekking pole standing on a rocky summit in silhouette, dark mountain ridges below a misty rust-orange sky"></div>
    <div class="brand">
      <span class="brand-dot"></span>
      <span class="brand-name">TrailKeeper</span>
    </div>
    <div class="member-details">
      <p class="member-name">MARCUS HALE</p>
      <p class="member-id">VIP-XXXXXXX</p>
    </div>
  </div>
</body>
</html>
```